Page lark & Glimmerly ad needed

I am in need of a simple static image ad to be used for Pagelark & Glimmerly. A photo of a nice roof on a nice house. "Instant Satellite Roof Estimates" "Your house, your time & instant estimate" . Our logo file is here: https://www.filquarry.com/scl/fo/t52wqpzx73hmbnvekcy8d/ZKqWT5PLmNdbX3HfGsYe8r2?rlkey=vn7cz2ktbw94pqdr6yjmfx4cs&dl=0

Multiple variations will be purchased.

```html
<!DOCTYPE html>
<html lang="en">
<head>
<meta charset="utf-8">
<title>Instant Satellite Roof Estimates</title>
<link href="https://fonts.googleapis.com/css2?family=Inter:wght@400;500;800&display=swap" rel="stylesheet">
<style>
  :root {
    --page-bg: #a9afbd;
    --card-bg: #ffffff;
    --navy: #0f2c6d;
    --ink: #2a2a2a;
    --logo-ink: #111111;
    --sky-top: #c6d8e8;
    --sky-low: #e6ecef;
    --roof: #4a4e58;
    --wall: #d9d2c6;
    --lawn: #7a9f4e;
  }
  * { margin: 0; padding: 0; box-sizing: border-box; }
  html, body {
    width: 1200px;
    height: 1200px;
    overflow: hidden;
    background: var(--page-bg);
    font-family: "Inter", Arial, sans-serif;
  }
  .ad-card {
    position: absolute;
    left: 102px;
    top: 0;
    width: 996px;
    height: 1200px;
    background: var(--card-bg);
    overflow: hidden;
  }
  .hero-photo {
    position: absolute;
    left: 0;
    top: 0;
    width: 996px;
    height: 643px;
    background: linear-gradient(180deg,
      var(--sky-top) 0%,
      var(--sky-low) 18%,
      var(--roof) 45%,
      var(--wall) 72%,
      var(--lawn) 100%);
  }
  .brand {
    position: absolute;
    left: 66px;
    top: 742px;
    display: flex;
    align-items: center;
    gap: 14px;
  }
  .brand-mark {
    width: 36px;
    height: 36px;
    border: 4px solid var(--logo-ink);
  }
  .brand-name {
    font-weight: 500;
    font-size: 40px;
    letter-spacing: 1px;
    color: var(--logo-ink);
    line-height: 1;
  }
  .headline {
    position: absolute;
    left: 68px;
    top: 840px;
    font-weight: 800;
    font-size: 98px;
    line-height: 100px;
    letter-spacing: 0;
    color: var(--navy);
    white-space: nowrap;
  }
  .tagline {
    position: absolute;
    left: 71px;
    top: 1058px;
    font-weight: 400;
    font-size: 43px;
    line-height: 52px;
    letter-spacing: 0.3px;
    color: var(--ink);
    white-space: nowrap;
  }
</style>
</head>
<body>
  <main class="ad-card">
    <div class="hero-photo" role="img" aria-label="Photograph of a modern single-storey house with a dark tiled gabled roof, light stucco walls, wood accents and a landscaped front lawn under a clear sky"></div>

    <div class="brand">
      <span class="brand-mark"></span>
      <span class="brand-name">HALDEN ROOFING</span>
    </div>

    <h1 class="headline">Instant Satellite<br>Roof Estimates</h1>

    <p class="tagline">Your house, your time &amp; instant estimate</p>
  </main>
</body>
</html>
```